Colm Brevik Interior Design

I need a web design/business card design(branding for company as a whole)for a San Francisco based interior design company. Looking for a clean and modern website that is not too modern. I have younger and older clients. I want my website to be easy to use and be able to group my different projects in one area along with having my pictures be the main focus of the website as that is my selling point. I would like my website to be in the black white silver and gold color scheme but open to other colors. I also want the website to feel playful

Target Market(s)

All types. Want the website to feel open and clean but warm at the same time
examples of work I like. http://www.olenstudio.example/ns/portfolio/design.php
Like many of the business card designs on this link. . really like the one card that has the message in it" hello, my name is" http://www.tillerpressworks.example/2011/03/black-business-cards/

http://www.vantor-bay.example/archives/home_2011_12_01.html

These links will give you an idea of the style I like. I want to do a die cut business card and want that type of look on my website as well. Want my branding to feel like a story to my clients. I like the interaction or theme that some of the examples have. I want people to pick up my business cards because the look cool and different. it's the small details that makes in difference in my business and I want that to show in my website and business card- and overall branding.

Industry/Entity Type

Business

Requirements
Must have
• Chatterlane link
Careernest link
plume link to my reviews
zibbo map of my office
snipwallia.example
contact form page

```html
<!DOCTYPE html>
<html lang="en">
<head>
<meta charset="utf-8">
<title>Colm Brevik Interior Design — Gallery</title>
<link rel="stylesheet" href="https://fonts.googleapis.com/css2?family=Open+Sans:wght@300;400&family=Arimo:wght@400&display=swap">
<style>
  :root {
    --bg: #1c1c1d;
    --bg-band: #222223;
    --rule: #3c3c3e;
    --nav: #9a9a9c;
    --nav-active: #f2f2f2;
    --contact: #5f5f61;
    --social: #7e7e80;
    --fine: #9a9a9a;
    --card: #ffffff;
    --card-title: #111111;
    --card-body: #666666;
  }
  * { margin: 0; padding: 0; box-sizing: border-box; }
  html, body { width: 1200px; height: 833px; overflow: hidden; background: var(--bg); }
  .page { position: relative; width: 1200px; height: 833px; overflow: hidden; background: var(--bg); }
  .backdrop { position: absolute; inset: 0; }

  .sidebar { position: absolute; left: 55px; top: 0; width: 235px; font-family: "Open Sans", sans-serif; }
  .brand { position: absolute; left: 1px; top: 26px; display: flex; align-items: center; gap: 7px; }
  .brand-mark { width: 73px; height: 73px; border: 4px solid #ffffff; border-radius: 50%; }
  .brand-name { color: #cfcfcf; font-weight: 300; font-size: 21px; line-height: 17px; letter-spacing: 0.3px; }
  .rule { position: absolute; left: 0; width: 235px; height: 1px; background: var(--rule); }
  .nav { position: absolute; left: 2px; top: 122px; list-style: none; }
  .nav li { font-weight: 300; font-size: 21px; line-height: 33.8px; color: var(--nav); }
  .nav li.is-active { color: var(--nav-active); }
  .contact { position: absolute; left: 3px; top: 310px; }
  .contact p { font-weight: 300; font-size: 18px; line-height: 33.6px; color: var(--contact); }
  .contact p.social { font-weight: 400; font-size: 20px; color: var(--social); }
  .copyright { position: absolute; left: 4px; top: 427px; font-family: "Arimo", sans-serif; font-size: 8px; color: var(--fine); }

  .gallery { position: absolute; left: 392px; top: 32.5px; display: grid; grid-template-columns: repeat(3, 203px); column-gap: 12px; row-gap: 17px; }
  .card { background: var(--card); width: 203px; height: 363px; padding: 5px 6.5px 0; font-family: "Arimo", sans-serif; }
  .card-photo { width: 190px; height: 237px; }
  .card-title { margin-top: 7px; font-size: 11.7px; line-height: 14px; color: var(--card-title); font-weight: 400; }
  .card-text { margin-top: 1px; font-size: 9.1px; line-height: 15px; color: var(--card-body); white-space: nowrap; }

  .photo-kitchen {
    background:
      radial-gradient(circle at 22% 28%, rgba(200,80,90,.35) 0, rgba(200,80,90,0) 22%),
      radial-gradient(circle at 70% 12%, rgba(180,190,190,.6) 0, rgba(180,190,190,0) 30%),
      linear-gradient(180deg, #eceded 0%, #d9d9d6 50%, #9c5e33 66%, #b57844 71%, #f3f3f3 80%, #e3e4e4 100%);
  }
  .photo-lounge {
    background:
      radial-gradient(ellipse at 15% 22%, rgba(150,100,70,.7) 0, rgba(150,100,70,0) 35%),
      radial-gradient(ellipse at 55% 70%, rgba(245,244,240,.9) 0, rgba(245,244,240,0) 30%),
      linear-gradient(180deg, #c9b59c 0%, #dcd6ce 42%, #c4c3c4 62%, #8f9097 100%);
  }
  .photo-reception {
    background:
      radial-gradient(circle at 55% 25%, rgba(200,205,215,.45) 0, rgba(200,205,215,0) 35%),
      radial-gradient(ellipse at 45% 60%, rgba(210,195,165,.8) 0, rgba(210,195,165,0) 30%),
      linear-gradient(180deg, #2c2e38 0%, #1e1d24 50%, #2a2428 75%, #141216 100%);
  }
  .photo-bedroom {
    background:
      radial-gradient(ellipse at 30% 15%, rgba(30,30,30,.75) 0, rgba(30,30,30,0) 25%),
      radial-gradient(ellipse at 40% 70%, rgba(160,170,50,.9) 0, rgba(160,170,50,0) 45%),
      linear-gradient(180deg, #d6c49d 0%, #ebe6da 40%, #c7c88a 62%, #f2f1ea 88%, #cbb99a 100%);
  }
  .photo-living {
    background:
      radial-gradient(ellipse at 42% 38%, rgba(170,200,120,.55) 0, rgba(170,200,120,0) 25%),
      radial-gradient(ellipse at 35% 82%, rgba(70,50,40,.55) 0, rgba(70,50,40,0) 20%),
      linear-gradient(180deg, #f3f1eb 0%, #e9e4d8 50%, #cdb79b 78%, #a78457 100%);
  }
  .photo-dining {
    background:
      radial-gradient(ellipse at 75% 18%, rgba(190,130,70,.8) 0, rgba(190,130,70,0) 40%),
      radial-gradient(ellipse at 40% 65%, rgba(246,242,234,.95) 0, rgba(246,242,234,0) 40%),
      linear-gradient(135deg, #c99e60 0%, #e6d9c6 40%, #efe8dc 65%, #d4c6b2 100%);
  }
</style>
</head>
<body>
<div class="page">
  <svg class="backdrop" width="1200" height="833" viewBox="0 0 1200 833" aria-hidden="true">
    <polygon points="290,0 1200,0 1200,235" fill="var(--bg-band)"/>
  </svg>

  <aside class="sidebar">
    <div class="brand">
      <div class="brand-mark"></div>
      <div class="brand-name">Colm<br>Brevik</div>
    </div>
    <div class="rule" style="top:117px"></div>
    <ul class="nav">
      <li>About Me</li>
      <li class="is-active">Gallery</li>
      <li>Real estate</li>
      <li>Blog</li>
      <li>Contact me</li>
    </ul>
    <div class="rule" style="top:300px"></div>
    <div class="contact">
      <p>hello@colmbrevik.example</p>
      <p>Phone: 415 555 0142</p>
      <p class="social">Chatterlane</p>
    </div>
    <div class="rule" style="top:420px"></div>
    <p class="copyright">© 2012 Colm Brevik .All rights reserved</p>
  </aside>

  <main class="gallery">
    <article class="card">
      <div class="card-photo photo-kitchen" role="img" aria-label="Photo of a white modern kitchen with wooden worktop and stainless hood"></div>
      <h2 class="card-title">Modern Kitchen for this summer !</h2>
      <p class="card-text">Many desktop publishing packages and web<br>page editors now use Lorem Ipsum as their<br>default model text, and a search for 'lorem<br>ipsum' will uncover many web sites still in their<br>infancy. Various versions have evolved over<br>the years</p>
    </article>
    <article class="card">
      <div class="card-photo photo-lounge" role="img" aria-label="Photo of a lounge with bookshelves, white table and patterned armchair"></div>
      <h2 class="card-title">Modern Kitchen for this summer !</h2>
      <p class="card-text">Many desktop publishing packages and web<br>page editors now use Lorem Ipsum as their<br>default model text, and a search for 'lorem<br>ipsum' will uncover many web sites still in their<br>infancy. Various versions have evolved over<br>the years</p>
    </article>
    <article class="card">
      <div class="card-photo photo-reception" role="img" aria-label="Photo of a dark reception desk with circular screen and stone counter"></div>
      <h2 class="card-title">Modern Kitchen for this summer !</h2>
      <p class="card-text">Many desktop publishing packages and web<br>page editors now use Lorem Ipsum as their<br>default model text, and a search for 'lorem<br>ipsum' will uncover many web sites still in their<br>infancy. Various versions have evolved over<br>the years</p>
    </article>
    <article class="card">
      <div class="card-photo photo-bedroom" role="img" aria-label="Photo of a low bed with green throw and framed art above"></div>
      <h2 class="card-title">Modern Kitchen for this summer !</h2>
      <p class="card-text">Many desktop publishing packages and web<br>page editors now use Lorem Ipsum as their<br>default model text, and a search for 'lorem<br>ipsum' will uncover many web sites still in their<br>infancy. Various versions have evolved over<br>the years</p>
    </article>
    <article class="card">
      <div class="card-photo photo-living" role="img" aria-label="Photo of a bright living room with sheer curtains and sculptural coffee table"></div>
      <h2 class="card-title">Modern Kitchen for this summer !</h2>
      <p class="card-text">Many desktop publishing packages and web<br>page editors now use Lorem Ipsum as their<br>default model text, and a search for 'lorem<br>ipsum' will uncover many web sites still in their<br>infancy. Various versions have evolved over<br>the years</p>
    </article>
    <article class="card">
      <div class="card-photo photo-dining" role="img" aria-label="Photo of a cream dining set in front of a wooden feature wall"></div>
      <h2 class="card-title">Modern Kitchen for this summer !</h2>
      <p class="card-text">Many desktop publishing packages and web<br>page editors now use Lorem Ipsum as their<br>default model text, and a search for 'lorem<br>ipsum' will uncover many web sites still in their<br>infancy. Various versions have evolved over<br>the years</p>
    </article>
  </main>
</div>
</body>
</html>
```